BROCHURE 16 PAGES WITH NICE DESIGN AND PHOTOS

We need a brochure design for a group of medical clinics that apply a new approach in medicine which is more personalised and is called Cellwise Clinics. Actually we need to show somehow our approach maybe with a nice design of the human body.

We utilise Metabolomic Analysis (advanced blood and urine analysis performed in few labs around the world).

Metabolomic Analyses are very precise and reveal all the actual health status of a person including all the deficiencies/imbalances inside the cells and all the chemical reactions. Metabolomic analyses show what the human body actual needs in order to perform in optimum level.
Then we deliver therapeutic regimen which includes appropriate nutrition scheme and restoration of the imbalances by administering vitamins, amino acids, fats, minerals, and medication where needed.
That way the body repairs and replenishes its deficiencies and imbalances and starts to function optimum.
This method has a great success rate in chronic and autoimmune diseases and is also great for prevention.

I attach a brochure which we are not very fond of.
It has the text we want to iclude in the brochure.
I attach also our logo
The brochure should not be less than 20*21cm.

Target Market(s)

35-65+ mostly women who want to to prevent disease and be, look and feel healthy. Also women and men who want to find a solution from their autoimmune and chronic condition.

Industry/Entity Type

Medical

Other font styles liked:
• AVENIR NEXT OR SIMILAR

Requirements
Must have
• telomeres, nice healthy looking woman, advanced lab
• also vitruvian woman and vitruvian man (innovative design)
• around 16 pages max, must be also delivered in pdf for website.

```html
<!DOCTYPE html>
<html lang="en">
<head>
<meta charset="utf-8">
<title>Cellwise Clinics brochure – pages 4–5</title>
<link rel="stylesheet" href="https://fonts.googleapis.com/css2?family=Nunito+Sans:wght@400;600;700&display=swap">
<style>
  :root{
    --bg:#e9e7e3;
    --paper:#ffffff;
    --navy:#1d3f80;
    --navy-deep:#16336d;
    --sky:#7fbde3;
    --ink:#4a4f57;
    --heading:#1f4c9a;
  }
  *{box-sizing:border-box;margin:0;padding:0}
  html,body{width:1200px;height:880px;overflow:hidden}
  body{background:var(--bg);font-family:"Nunito Sans",Arial,sans-serif;color:var(--ink);position:relative}
  .spread{position:absolute;left:60px;top:156px;width:1080px;height:567px;display:flex;box-shadow:0 10px 30px rgba(0,0,0,.18)}
  .page{position:relative;width:540px;height:567px;background:var(--paper);overflow:hidden}
  .page--left{box-shadow:inset -18px 0 22px -18px rgba(0,0,0,.18)}
  .page--right{box-shadow:inset 18px 0 22px -18px rgba(0,0,0,.14)}

  .photo{position:absolute}
  .photo--concept{left:0;top:0;width:540px;height:170px;
    background:linear-gradient(180deg,#b9d3e6 0%,#d2e2ee 60%,rgba(255,255,255,0) 100%)}
  .photo--portrait{left:0;top:0;width:300px;height:205px;
    background:linear-gradient(90deg,#ffffff 0%,#eef3f7 40%,#c8dbe9 100%)}
  .panel--sky{position:absolute;left:300px;top:0;width:240px;height:240px;
    background:linear-gradient(180deg,#9cc1dc 0%,#7fa9cb 70%,rgba(127,169,203,0) 100%)}
  .panel--fade{position:absolute;left:0;top:0;width:300px;height:205px;
    background:linear-gradient(180deg,rgba(255,255,255,0) 80%,#ffffff 100%)}
  .photo--family{right:20px;top:403px;width:220px;height:84px;
    background:linear-gradient(180deg,#f3f5f7,#e3e9ee)}

  .title{position:absolute;left:36px;top:128px;font-size:15px;line-height:16px;font-weight:700;color:var(--heading);text-transform:uppercase;letter-spacing:-.2px}
  .col{position:absolute;width:222px;font-size:8.6px;line-height:11.5px}
  .col p{margin-bottom:9px}
  .col p:last-child{margin-bottom:0}
  .col--l1{left:36px;top:172px}
  .col--l2{left:282px;top:172px}
  .col--r1{left:36px;top:222px;width:226px}
  .col--r2{left:288px;top:248px;width:222px}

  .footer{position:absolute;left:0;bottom:0;width:540px;height:80px;background:linear-gradient(180deg,var(--navy),var(--navy-deep))}
  .pagenum{position:absolute;bottom:0;width:46px;height:80px;background:var(--sky);color:#fff;font-size:17px;font-weight:600;display:flex;align-items:flex-end;justify-content:center;padding-bottom:14px}
  .page--left .pagenum{left:40px}
  .page--right .pagenum{right:40px}
  .brand{position:absolute;display:flex;align-items:center;gap:9px;color:#fff}
  .brand__dot{width:24px;height:24px;border-radius:50%;background:#fff;flex:none}
  .brand__name{font-size:15px;font-weight:700;letter-spacing:.2px;line-height:15px}
  .brand__tag{font-size:5px;letter-spacing:1px;text-transform:uppercase;line-height:8px}
  .page--left .brand{left:110px;top:28px}
  .page--right .brand{left:178px;top:28px}
  .contact{position:absolute;color:#fff;font-size:8.5px;line-height:11px}
  .page--left .contact{right:24px;top:24px}
  .page--right .contact{left:34px;top:18px;text-align:right}
</style>
</head>
<body>
<main class="spread">
  <section class="page page--left">
    <div class="photo photo--concept" role="img" aria-label="Concept photo: a hand touching glowing hexagons labelled nutrients, telomeres, energy and natural on a pale blue background"></div>
    <h2 class="title">Autoimmune &amp;<br>Chronic Diseases</h2>
    <div class="col col--l1">
      <p>Cells are the basic building blocks of a human body, which is composed of trillions of cells. They form the organs and the tissues, take in nutrients from food, convert those nutrients into energy, and carry out specialised functions. Components like minerals, amino acids, proteins, vitamins, enzymes, fat, and carbohydrates are essential for normal cellular function.</p>
      <p>Cells seek their energy in the form of food molecules and sunlight. Then they generate energy according to the components they have in stock. The operating condition of our cells reflects our general health status.</p>
      <p>But can food in the modern world provide all those important compounds a cell needs in quantity and</p>
    </div>
    <div class="col col--l2">
      <p>quality, to construct its tissues and perform the cellular functions for a healthy human body?</p>
      <p>Within just fifty years, food has undergone an enormous change due to over cultivation and thus soil depletion is immense. To increase production and meet demand, the use of fertilisers that restore the necessary components of the ground is unavoidable. In no case though can fertilisers provide the 92 elements available in nature.</p>
      <p>Conventional cultivations enrich soil using fertilisers containing three critical components for plant growth (nitrogen, potassium, and phosphorus) whereas the best organic crops reach up to merely sixteen.</p>
      <p>We are in a condition that modern man is starving although there is an abundance of food. Also, apart from the deficiencies cells present, they are also burdened with toxic substances that should not be present within them. Xenobiotic substances like</p>
    </div>
    <footer class="footer">
      <div class="brand">
        <span class="brand__dot"></span>
        <div><div class="brand__name">CELLWISE CLINICS</div><div class="brand__tag">Health clinics for autoimmune and chronic diseases</div></div>
      </div>
      <div class="contact">info@cellwiseclinics.com<br>www.cellwiseclinics.com<br>www.drmarenhollis.com</div>
    </footer>
    <div class="pagenum">4</div>
  </section>

  <section class="page page--right">
    <div class="panel--sky"></div>
    <div class="photo photo--portrait" role="img" aria-label="Photo of a smiling healthy young woman against a soft blue background"></div>
    <div class="panel--fade"></div>
    <div class="col col--r1">
      <p>heavy metals, industrial chemicals, drugs and other toxic elements alter the biochemical balance of the cell.</p>
      <p>Gradually, significant deficiencies and toxic accumulation are created at a cellular and molecular level and manifest in the form of a disease or a chronic condition.</p>
      <p>The alteration in the biochemical composition of the cells is accompanied by a change in how those cells are perceived from the immune system. As a result of the above, the body does not recognise its own cells and attacks them.</p>
      <p>Depending on heredity, environment, and dietary choices, cells that deviate the most from normal are the first ones to be attacked. That's the reason why in many cases, the body attacks more than one organs or systems.</p>
      <p>The main causes for the manifestation of an</p>
    </div>
    <div class="col col--r2">
      <p>autoimmune disease are two: cellular deficiency and cellular toxicity. Cells with nutritional deficiencies or exposed to toxic substances malfunction.</p>
      <p>Preventing or reversing autoimmunity is about preventing and reversing cellular deficiencies and toxicities and thus restoring natural functioning.</p>
      <p>Restoration of healthy cell functions with the use of the recommended nutraceutical and pharmaceutical treatment is the most efficient tool for autoimmune conditions, chronic diseases, and prevention.</p>
    </div>
    <div class="photo photo--family" role="img" aria-label="Photo of a smiling family and a female doctor with a stethoscope"></div>
    <footer class="footer">
      <div class="contact">info@cellwiseclinics.com<br>www.cellwiseclinics.com<br>www.drmarenhollis.com</div>
      <div class="brand">
        <span class="brand__dot"></span>
        <div><div class="brand__name">CELLWISE CLINICS</div><div class="brand__tag">Health clinics for autoimmune and chronic diseases</div></div>
      </div>
    </footer>
    <div class="pagenum">5</div>
  </section>
</main>
</body>
</html>
```